Adventurous female pilot

I am looking for a personal business card, for a very well qualified female pilot, with a lot of aviation experience.

Currently an airline pilot, have worked as a bush pilot in Africa, looking to get into corporate aviation, or private jet owners.
Want a classy looking card for networking...

Could be interested in a retro\vintage look also?!

An idea,, is an african sunset background, with my wings\logo on it
Updates

I just want to say thank you to all of your for your amazing designs!

I have been very busy flying this past week , so not had a chance to be on the computer much.
But I provide some feedback, and conclusions very soon!
Thank you again.

Marla

Reason: Still waiting on a couple of revisions to be 100% about my choice!

Target Market(s)

corporate aviation, private jet owners, casino's,
General audience.
networking

Industry/Entity Type

Airline

Requirements
Nice to have
• Classy, edgy, sexy, but also feminine

```html
<!DOCTYPE html>
<html lang="en">
<head>
<meta charset="utf-8">
<title>Marla Vance – Business Card</title>
<link rel="stylesheet" href="https://fonts.googleapis.com/css2?family=Cormorant+Garamond:ital,wght@1,500&display=swap">
<style>
  :root {
    --page-bg: #ece6dc;
    --sky-top: #5e1608;
    --sky-mid: #b2420c;
    --sky-glow: #e98a10;
    --sun: #f6a816;
    --horizon: #7a2a08;
    --ground: #1a0a04;
    --ink-light: #fbf4ea;
  }
  * { margin: 0; padding: 0; box-sizing: border-box; }
  html, body {
    width: 1200px;
    height: 1000px;
    overflow: hidden;
    background: var(--page-bg);
  }
  .canvas {
    position: relative;
    width: 1200px;
    height: 1000px;
    display: flex;
    align-items: center;
    justify-content: center;
  }
  .business-card {
    position: relative;
    width: 900px;
    height: 514px;
    border-radius: 14px;
    overflow: hidden;
    font-family: "Cormorant Garamond", Georgia, serif;
    font-style: italic;
    font-weight: 500;
    color: var(--ink-light);
  }
  .savanna-sunset {
    position: absolute;
    inset: 0;
    background:
      radial-gradient(circle at 66% 24%, var(--sun) 0, var(--sun) 15%, rgba(246,168,22,0.55) 22%, rgba(246,168,22,0) 38%),
      linear-gradient(180deg,
        var(--sky-top) 0%,
        var(--sky-mid) 30%,
        var(--sky-glow) 58%,
        var(--horizon) 76%,
        var(--ground) 86%,
        var(--ground) 100%);
  }
  .brand-mark {
    position: absolute;
    left: 110px;
    top: 118px;
    font-size: 46px;
    line-height: 1;
    color: var(--ink-light);
  }
  .card-name {
    position: absolute;
    left: 455px;
    top: 238px;
    font-size: 46px;
    line-height: 1;
  }
  .card-email {
    position: absolute;
    left: 458px;
    top: 296px;
    font-size: 31px;
    line-height: 1;
  }
  .card-phone {
    position: absolute;
    font-size: 29px;
    line-height: 1;
  }
  .card-phone--taipei { left: 470px; top: 392px; }
  .card-phone--us { left: 66px; top: 462px; }
</style>
</head>
<body>
  <main class="canvas">
    <article class="business-card">
      <div class="savanna-sunset" role="img" aria-label="African savanna at sunset with a large orange sun, acacia trees, an elephant and giraffes in silhouette"></div>
      <div class="brand-mark">Vance Wings</div>
      <h1 class="card-name">Marla Vance</h1>
      <p class="card-email">Email: marlacvance@skyroute.net</p>
      <p class="card-phone card-phone--taipei">Cell Taipei: +886 912-406-238</p>
      <p class="card-phone card-phone--us">Cell US: +1 702-555-0148</p>
    </article>
  </main>
</body>
</html>
```